Harlow Mesa Podiatry
Business card, letterhead & envelope
Professional
4631 NW 52nd St
Suite 310
Alder Springs, GA 32786
mtollanddpm@brindlemail.com
Front of Card should also have names of doctors:
Marcus Tolland, DPM
Lanh T. Vu, DPM
Back of card should have information for appointment:
1. Date
2. Time
3. Day of week to circle (ie Mon, Tues, Wed, Thurs, Fri)
4. "If unable to keep appointment kindly give 24 hours notice"
Logo designs for Harlow Mesa Podiatry

```html
<!DOCTYPE html>
<html lang="en">
<head>
<meta charset="utf-8">
<title>Harlow Mesa Podiatry – Stationery</title>
<link href="https://fonts.googleapis.com/css2?family=Arimo:wght@400;700&display=swap" rel="stylesheet">
<style>
  :root{
    --green:#7cb92a;
    --green-dark:#5f9418;
    --ink:#1f1f1f;
    --muted:#555555;
    --paper:#ffffff;
    --backdrop:#d9d9d9;
  }
  *{box-sizing:border-box;margin:0;padding:0}
  html,body{width:1200px;height:912px;overflow:hidden}
  body{background:var(--backdrop);font-family:"Arimo",Arial,sans-serif;color:var(--ink);position:relative}
  address{font-style:normal}

  .brand{font-weight:700;text-transform:uppercase;line-height:1.02;letter-spacing:.5px;display:flex;align-items:flex-start;gap:7px;color:var(--green-dark);background:var(--paper)}
  .brand-mark{width:12px;height:12px;background:currentColor;flex:none;margin-top:3px}

  .sheet{position:absolute;background:var(--paper);overflow:hidden;box-shadow:0 2px 6px rgba(0,0,0,.18)}
  .band{position:absolute;left:0;right:0;background:var(--green)}
  .email{color:var(--green-dark)}

  /* Envelope */
  .envelope{left:40px;top:30px;width:560px;height:243px}
  .envelope .band{top:32px;height:26px}
  .envelope .brand{position:absolute;left:16px;top:20px;font-size:20px;padding:8px 10px}
  .envelope-contact{position:absolute;left:26px;top:128px;font-size:12px;line-height:1.45}
  .envelope-contact .phone{margin-top:10px}

  /* Card front */
  .card-front{left:40px;top:305px;width:350px;height:200px}
  .card-front .band{top:24px;height:20px}
  .card-front .brand{position:absolute;left:12px;top:12px;font-size:16px;padding:7px 9px}
  .card-address{position:absolute;left:170px;top:72px;font-size:10.5px;line-height:1.45}
  .card-doctors{position:absolute;left:22px;top:148px;font-size:10.5px;line-height:1.45}
  .card-doctors .second{color:var(--green-dark)}
  .card-contact{position:absolute;left:170px;top:148px;font-size:10.5px;line-height:1.45}

  /* Card back */
  .card-back{left:40px;top:530px;width:350px;height:200px;background:var(--green);color:#fff;padding:20px 22px}
  .card-back .brand{position:absolute;right:22px;top:18px;font-size:13px;color:#fff;background:none}
  .appt-row{display:flex;align-items:flex-end;gap:8px;font-size:12px;margin-bottom:14px}
  .appt-line{flex:none;width:130px;border-bottom:1px solid #fff;height:13px}
  .days{display:flex;gap:12px;font-size:11px;margin:16px 0 14px}
  .day{display:flex;align-items:center;gap:4px}
  .day-box{width:9px;height:9px;border:1px solid #fff}
  .notice{font-size:10.5px;border-top:1px solid rgba(255,255,255,.6);padding-top:9px}

  /* Letterhead */
  .letterhead{left:640px;top:30px;width:520px;height:673px}
  .letterhead .band{left:150px;top:28px;height:24px}
  .letterhead .brand{position:absolute;left:16px;top:20px;font-size:20px}
  .letterhead-body{position:absolute;left:80px;right:30px;top:120px;font-size:9.5px;line-height:1.55;color:var(--muted)}
  .letterhead-body h2{font-size:10px;color:var(--ink);font-weight:700;margin-bottom:22px}
  .letterhead-body p{margin-bottom:12px;text-align:justify}
  .letterhead-contact{position:absolute;left:20px;bottom:26px;font-size:11px;line-height:1.45}
  .letterhead-contact .phone{margin-top:10px}
</style>
</head>
<body>

<section class="sheet envelope">
  <div class="band"></div>
  <div class="brand"><span class="brand-mark"></span><span>Harlow<br>Mesa<br>Podiatry</span></div>
  <address class="envelope-contact">
    4631 NW 52nd St<br>Suite 310<br>Alder Springs, GA 32786
    <div class="phone">(470) 555-0148</div>
    <div class="email">frontdesk@harlowmesapodiatry.com</div>
  </address>
</section>

<section class="sheet card-front">
  <div class="band"></div>
  <div class="brand"><span class="brand-mark"></span><span>Harlow<br>Mesa<br>Podiatry</span></div>
  <address class="card-address">4631 NW 52nd St<br>Suite 310<br>Alder Springs, GA 32786</address>
  <div class="card-doctors">Marcus Tolland, DPM<br><span class="second">Lanh T. Vu, DPM</span></div>
  <div class="card-contact">(470) 555-0148<br><span class="email">frontdesk@harlowmesapodiatry.com</span></div>
</section>

<section class="sheet card-back">
  <div class="brand"><span class="brand-mark"></span><span>Harlow<br>Mesa<br>Podiatry</span></div>
  <div class="appt-row">Date: <span class="appt-line"></span></div>
  <div class="appt-row">Time: <span class="appt-line"></span></div>
  <div class="days">
    <span class="day"><span class="day-box"></span>Mon</span>
    <span class="day"><span class="day-box"></span>Tues</span>
    <span class="day"><span class="day-box"></span>Wed</span>
    <span class="day"><span class="day-box"></span>Thurs</span>
    <span class="day"><span class="day-box"></span>Fri</span>
  </div>
  <p class="notice">If unable to keep appointment kindly give 24 hours notice</p>
</section>

<section class="sheet letterhead">
  <div class="band"></div>
  <div class="brand"><span class="brand-mark"></span><span>Harlow<br>Mesa<br>Podiatry</span></div>
  <div class="letterhead-body">
    <h2>Lorem ipsum</h2>
    <p>Thank you for choosing our practice for your foot and ankle care. We look forward to seeing you at your next visit.</p>
    <p>Our team offers gentle, thorough treatment for heel pain, sports injuries, diabetic foot care and custom orthotics for patients of every age.</p>
    <p>Please bring your insurance card, a list of current medications and any recent imaging to your appointment so we can plan your care.</p>
    <p>If you have questions before your visit, call our office and a member of our staff will be glad to help you.</p>
    <p>Our office is open Monday through Friday, and same week visits are often available for new and returning patients.</p>
  </div>
  <address class="letterhead-contact">
    4631 NW 52nd St<br>Suite 310<br>Alder Springs, GA 32786
    <div class="phone">(470) 555-0148</div>
    <div class="email">frontdesk@harlowmesapodiatry.com</div>
  </address>
</section>

</body>
</html>
```